Salt Moon, Tin Heart

Hey Guys
Please visit our Chatterleaf page for the film. See what ideas you bring to the table for the movie poster.
Looking for creative and something fresh.
Check out cast on QVTK
Will use the stills from the film for actual poster and quality.
Thanks a million for taking an interest in our film. xoxo
Target Market(s)
2-50 year old, date night, girls night out
Industry/Entity Type
Movie

```html
<!DOCTYPE html>
<html lang="en">
<head>
<meta charset="utf-8">
<title>Salt Moon, Tin Heart — Poster</title>
<link rel="stylesheet" href="https://fonts.googleapis.com/css2?family=Montserrat:wght@500;600&family=Oswald:wght@400&display=swap">
<style>
  :root {
    --header-bg: #e3ebf3;
    --stripe: #4e6a7e;
    --ink: #111111;
    --accent: #f2505f;
    --tagline: #3b5a6e;
    --credit: #f2f4f7;
    --water: #c7d3d9;
  }
  html, body { margin: 0; padding: 0; overflow: hidden; background: #ffffff; }
  .poster {
    position: relative;
    width: 810px;
    height: 1200px;
    overflow: hidden;
    font-family: "Montserrat", sans-serif;
    background: var(--header-bg);
  }
  .cast {
    position: absolute;
    top: 0; left: 0;
    width: 810px; height: 82px;
    background: var(--header-bg);
  }
  .cast-member {
    position: absolute;
    top: 25px;
    width: 190px;
    margin-left: -95px;
    text-align: center;
    line-height: 1;
  }
  .cast-first { display: block; font-size: 16px; font-weight: 500; color: var(--ink); }
  .cast-last { display: block; font-size: 26px; font-weight: 600; color: var(--accent); margin-top: 3px; letter-spacing: 0.2px; }
  .stripe { position: absolute; left: 0; width: 810px; height: 8px; background: var(--stripe); }
  .stripe-top { top: 82px; }
  .stripe-bottom { top: 544px; }
  .still {
    position: absolute;
    top: 90px; left: 0;
    width: 810px; height: 454px;
    background:
      radial-gradient(ellipse 170px 200px at 330px 330px, rgba(228,196,172,0.85), rgba(228,196,172,0) 100%),
      radial-gradient(ellipse 150px 220px at 160px 360px, rgba(214,184,140,0.75), rgba(214,184,140,0) 100%),
      radial-gradient(ellipse 260px 120px at 390px 40px, rgba(92,72,58,0.75), rgba(92,72,58,0) 100%),
      radial-gradient(ellipse 150px 200px at 520px 170px, rgba(214,176,152,0.75), rgba(214,176,152,0) 100%),
      radial-gradient(ellipse 150px 210px at 780px 100px, rgba(150,146,116,0.8), rgba(150,146,116,0) 100%),
      linear-gradient(180deg, #d4dde1 0%, var(--water) 30%, #cbd6dc 100%);
  }
  .backdrop {
    position: absolute;
    top: 552px; left: 0;
    width: 810px; height: 648px;
    background: linear-gradient(180deg, #dde8f2 0%, #e6eef5 55%, #eadbe3 72%, #e8c9d3 78%, #9fa8b3 80%, #6f7680 84%, #a89e98 88%, #b9aca3 100%);
  }
  .title {
    position: absolute;
    left: 0; top: 589px;
    width: 810px;
    margin: 0;
    font-weight: 600;
    font-size: 100px;
    line-height: 1;
    letter-spacing: -1px;
  }
  .title-line { display: block; white-space: nowrap; }
  .title-line-one { color: var(--ink); padding-left: 50px; }
  .title-line-two { color: var(--accent); padding-left: 205px; margin-top: 20px; }
  .tagline {
    position: absolute;
    left: 190px; top: 897px;
    margin: 0;
    font-size: 21px;
    font-weight: 500;
    color: var(--tagline);
  }
  .credits {
    position: absolute;
    left: 66px; top: 1122px;
    width: 500px;
    font-family: "Oswald", sans-serif;
    font-size: 13.5px;
    line-height: 21px;
    color: var(--credit);
    letter-spacing: -0.3px;
    transform: scaleX(0.86);
    transform-origin: left top;
    white-space: nowrap;
  }
  .credits small { font-size: 6px; letter-spacing: 0; }
</style>
</head>
<body>
  <main class="poster">
    <header class="cast">
      <div class="cast-member" style="left:142px"><span class="cast-first">Tessa</span><span class="cast-last">MARLOWE</span></div>
      <div class="cast-member" style="left:326px"><span class="cast-first">Corin</span><span class="cast-last">VALE</span></div>
      <div class="cast-member" style="left:501px"><span class="cast-first">Elise</span><span class="cast-last">HARWICK</span></div>
      <div class="cast-member" style="left:676px"><span class="cast-first">D. Fenton</span><span class="cast-last">ASHBY</span></div>
    </header>
    <div class="stripe stripe-top"></div>
    <div class="still" role="img" aria-label="Film still: a couple touching foreheads by the water"></div>
    <div class="stripe stripe-bottom"></div>
    <div class="backdrop" role="img" aria-label="Dusk sky over a beach with a couple kissing by the shoreline"></div>
    <h1 class="title">
      <span class="title-line title-line-one">SALT MOON,</span>
      <span class="title-line title-line-two">TIN HEART</span>
    </h1>
    <p class="tagline">Fake it till you make it</p>
    <div class="credits">
      STUDIO NAME PICTURES <small>PRESENTS A</small> PRODUCERS <small>A FILM BY</small> SCRIPT WRITER ACTOR ONE ACTOR TWO "SALT MOON, TIN HEART"<br>
      <small>MUSIC BY</small> THE MUSICIAN <small>COSTUME</small> DESIGNER NAME <small>EDITED BY</small> EDITORS NAME <small>PRODUCTION</small> DESIGNERS NAME <small>DIRECTOR OF</small> CINEMATOGRAPHER<br>
      <small>EXECUTIVE</small> EX PRODUCER <small>PRODUCED BY</small> PRODUCER ONE PRODUCER 2 <small>STORY BY</small> STORY WRITER <small>SCREENPLAY BY</small> SCREEN WRITER <small>DIRECTED BY</small> DIRECTOR NAME
    </div>
  </main>
</body>
</html>
```